Basic business card

use my newly created logo - and the phrases (Faster Wafer Sort & Streamlined Device Qualification Support) - and my new email domain / ID - use at conferences / tradeshows

Industry/Entity Type

semiconductor

Contact Information for Business Card

Dale J Whitcomb, Owner, communicate via Logo - Lower COT - Cost of Test, Accelerated NPI - New Product Introduction, phone +1 555 014 6208, Larkfield, Oregon, USA, dale.whitcomb@vexlora.com

Font styles to use
Sans Serif

Requirements
Nice to have
• re-use my logo created via Pixel Harbor last August (#6182935)

```html
<!DOCTYPE html>
<html lang="en">
<head>
<meta charset="utf-8">
<title>Vexlora business card</title>
<link href="https://fonts.googleapis.com/css2?family=Montserrat:wght@400;500;700;800&display=swap" rel="stylesheet">
<style>
  :root {
    --stage: #2b2c2f;
    --card-white: #ffffff;
    --card-navy: #4a5878;
    --navy-ink: #2f3d63;
    --body-ink: #3b4456;
    --accent-blue: #1572c0;
    --accent-orange: #f0962e;
    --accent-green: #7cb82f;
    --tagline: #e6eaf2;
  }
  * { box-sizing: border-box; margin: 0; padding: 0; }
  html, body {
    width: 1200px; height: 900px; overflow: hidden;
    background: var(--stage);
    font-family: "Montserrat", sans-serif;
  }
  .sheet {
    position: relative; width: 1200px; height: 900px;
    display: flex; flex-direction: column; align-items: center; justify-content: center; gap: 40px;
  }
  .card {
    position: relative; width: 700px; height: 400px; border-radius: 28px; overflow: hidden;
    box-shadow: 0 12px 30px rgba(0,0,0,0.45);
  }

  /* Front */
  .card--front { background: var(--card-white); }
  .wordmark {
    display: flex; align-items: center; gap: 14px;
    font-weight: 500; letter-spacing: 0.04em; white-space: nowrap;
  }
  .wordmark__square { width: 22px; height: 22px; background: var(--accent-blue); }
  .card--front .wordmark {
    position: absolute; left: 150px; top: 62px;
    font-size: 42px; color: var(--navy-ink);
  }
  .person { position: absolute; left: 0; top: 140px; }
  .person__bar {
    position: absolute; left: 80px; top: 4px; width: 34px; height: 34px; background: var(--accent-blue);
  }
  .person__name {
    position: absolute; left: 130px; top: 0; white-space: nowrap;
    font-size: 30px; font-weight: 800; color: var(--navy-ink);
  }
  .person__role {
    position: absolute; left: 130px; top: 42px;
    font-size: 17px; font-weight: 400; color: var(--body-ink);
  }
  .contacts {
    position: absolute; left: 110px; top: 232px; list-style: none;
    display: flex; flex-direction: column; gap: 14px;
  }
  .contacts__item {
    display: flex; align-items: center; gap: 12px; white-space: nowrap;
    font-size: 17px; color: var(--body-ink);
  }
  .contacts__icon { width: 18px; height: 18px; flex: none; }

  /* Back */
  .card--back {
    background: var(--card-navy);
    display: flex; flex-direction: column; align-items: center; justify-content: center; gap: 26px;
  }
  .card--back .wordmark { font-size: 64px; color: var(--card-white); }
  .card--back .wordmark__square { width: 32px; height: 32px; }
  .tagline {
    font-size: 17px; font-weight: 400; color: var(--tagline); letter-spacing: 0.02em;
    white-space: nowrap; text-align: center;
  }
</style>
</head>
<body>
<main class="sheet">

  <section class="card card--front" aria-label="Business card front">
    <div class="wordmark"><span class="wordmark__square"></span><span>VEXLORA</span></div>

    <div class="person">
      <span class="person__bar"></span>
      <h1 class="person__name">Dale J Whitcomb</h1>
      <p class="person__role">Owner</p>
    </div>

    <ul class="contacts">
      <li class="contacts__item">
        <svg class="contacts__icon" viewBox="0 0 24 24" aria-hidden="true">
          <path fill="var(--accent-orange)" d="M6.6 10.8c1.4 2.8 3.8 5.1 6.6 6.6l2.2-2.2c.3-.3.7-.4 1-.2 1.1.4 2.3.6 3.600.6.6 0 1 .4 1 1V20c0 .6-.4 1-1 1C10.6 21 3 13.4 3 4c0-.6.4-1 1-1h3.5c.6 0 1 .4 1 1 0 1.3.2 2.5.6 3.6.1.3 0 .7-.2 1z"/>
        </svg>
        <span>+1 555 014 6208</span>
      </li>
      <li class="contacts__item">
        <svg class="contacts__icon" viewBox="0 0 24 24" aria-hidden="true">
          <rect x="2" y="5" width="20" height="14" rx="1.5" fill="var(--accent-blue)"/>
          <path d="M3 6.5l9 6.5 9-6.5" fill="none" stroke="#fff" stroke-width="1.8"/>
        </svg>
        <span>dale.whitcomb@vexlora.com</span>
      </li>
      <li class="contacts__item">
        <svg class="contacts__icon" viewBox="0 0 24 24" aria-hidden="true">
          <path fill="var(--accent-green)" d="M12 2a7 7 0 0 0-7 7c0 5.2 7 13 7 13s7-7.8 7-13a7 7 0 0 0-7-7zm0 9.5A2.5 2.5 0 1 1 12 6.5a2.5 2.5 0 0 1 0 5z"/>
        </svg>
        <span>Larkfield, Oregon, USA</span>
      </li>
    </ul>
  </section>

  <section class="card card--back" aria-label="Business card back">
    <div class="wordmark"><span class="wordmark__square"></span><span>VEXLORA</span></div>
    <p class="tagline">Faster Wafer Sort &amp; Streamlined Device Qualification Support</p>
  </section>

</main>
</body>
</html>
```